Website redesign for a technology and engineering company

We'd like to redesign our website which can be found on quorvane.co.nz
!! Please find the designers brief as an uploaded file with all details in there!!
The main purpose for redesign is:
>change of services offered
>old website not very user friendly to maintain or update
Key requirements:
>visually appealing
>easy to navigate
>simple and easy to read
>responsive
>mobile device compatibility
>integrating best SEO practice
All the details are in the attached designer brief document.

```html
<!DOCTYPE html>
<html lang="en">
<head>
<meta charset="utf-8">
<title>Quorvane — Precision. Efficiency. Clarity.</title>
<link href="https://fonts.googleapis.com/css2?family=Poppins:wght@400;500;600;700&display=swap" rel="stylesheet">
<style>
:root{
  --ink:#0b0b0b;
  --paper:#ffffff;
  --muted:#6f6f6f;
  --line:#cfcfcf;
  --card-dark:#1c2430;
}
*{box-sizing:border-box;margin:0;padding:0}
html,body{width:1200px;height:3907px;overflow:hidden}
body{position:relative;background:var(--paper);font-family:'Poppins',sans-serif;color:var(--ink)}
.abs{position:absolute}
.mark-dot{position:absolute;width:22px;height:22px;border-radius:50%;background:var(--ink)}
.mark-dot.light{background:var(--paper)}
a{color:inherit;text-decoration:none}

/* top bar + header */
.topbar{position:absolute;left:0;top:0;width:1200px;height:27px}
.topbar .contact-item{position:absolute;top:5px;color:var(--paper);font-size:12px;font-weight:500;display:flex;align-items:center;gap:8px}
.brand{position:absolute;font-weight:600;font-size:36px;letter-spacing:.5px;color:var(--ink)}
.nav{position:absolute;top:58px;left:642px;display:flex;gap:22px;font-size:14px;font-weight:500}
.nav a:first-child{font-weight:600}
.btn{position:absolute;display:flex;align-items:center;justify-content:center;gap:8px;font-size:14px;font-weight:600}
.btn-outline{border:1.5px solid var(--ink);background:var(--paper);color:var(--ink)}
.btn-dark{background:var(--ink);color:var(--paper)}
.btn-light{background:var(--paper);color:var(--ink)}

/* hero */
.hero{position:absolute;left:0;top:109px;width:1200px;height:730px;background:linear-gradient(160deg,#6d6d70 0%,#a9aaad 35%,#d4d5d8 60%,#8d8e91 100%)}
.hero h1{position:absolute;top:198px;left:0;width:1200px;text-align:center;color:var(--paper);font-size:73px;line-height:74px;font-weight:700;letter-spacing:.5px}

/* about */
.photo{position:absolute}
.badge{position:absolute;left:354px;top:1099px;width:98px;height:98px;border-radius:50%;background:var(--ink);border:3px solid var(--paper);color:var(--paper);display:flex;align-items:center;justify-content:center;font-size:17px;font-weight:600}
.section-title{position:absolute;font-size:42px;font-weight:600;line-height:1}
.rule{position:absolute;height:2px;width:70px;background:var(--ink)}
.about-copy{position:absolute;left:667px;top:1102px;width:340px;font-size:12px;line-height:16px;color:var(--muted)}

/* services */
.service{position:absolute;top:1591px;width:337px;height:472px;overflow:hidden}
.service-field{left:88px}
.service-positioning{left:431px}
.service-design{left:774px}
.service .label{position:absolute;left:0;bottom:14px;width:100%;text-align:center;color:var(--paper);font-size:23px;font-weight:600}
.service.dark{background:linear-gradient(180deg,#1b2636,#2a3442 60%,#20262e)}
.service.dark h3{margin-top:80px;text-align:center;color:var(--paper);font-size:23px;font-weight:600}
.service.dark ul{list-style:none;margin-top:16px;text-align:center;color:var(--paper);font-size:14px;line-height:26.5px}

/* case studies */
.case-card{position:absolute;left:121px;top:2280px;width:350px;height:270px;background:var(--paper);border-left:3px solid var(--ink);box-shadow:0 14px 34px rgba(0,0,0,.1);padding:26px 20px 0 18px}
.case-card h4{font-size:16px;font-weight:600;line-height:20px}
.case-card p{margin-top:10px;font-size:12px;line-height:16px;color:var(--muted)}
.arrows{display:flex;gap:8px;margin-top:14px}
.arrows span{width:29px;height:29px;border-radius:50%;border:1.5px solid var(--ink);display:flex;align-items:center;justify-content:center}
.arrows span.off{border-color:#999}

/* quote */
.quote{position:absolute;left:0;top:2680px;width:1200px;height:877px;background:var(--ink)}
.field{position:absolute;border-bottom:1.5px solid #8a8a8a;color:#e9e9e9;font-size:14px;padding-bottom:10px}

/* footer */
.footer{position:absolute;left:0;top:3557px;width:1200px;height:350px;background:var(--ink);color:var(--paper)}
.footer h5{position:absolute;font-size:23px;font-weight:600}
.footer .links{position:absolute;left:502px;top:84px;list-style:none;font-size:12.5px;line-height:26.5px}
.newsletter{position:absolute;left:739px;top:88px;width:350px;height:49px;background:var(--paper);color:#777;font-size:13px;display:flex;align-items:center;justify-content:space-between;padding:0 20px 0 22px}
</style>
</head>
<body>

<!-- top bar -->
<svg class="topbar" viewBox="0 0 1200 27" aria-hidden="true"><polygon points="560,0 1200,0 1200,27 539,27" fill="#0b0b0b"/></svg>
<div class="topbar">
  <div class="contact-item" style="left:726px">
    <svg width="14" height="10" viewBox="0 0 14 10"><rect width="14" height="10" rx="1" fill="#fff"/><path d="M0 1l7 5 7-5" stroke="#0b0b0b" stroke-width="1.4" fill="none"/></svg>
    hi@quorvane.nz
  </div>
  <div class="abs" style="left:881px;top:6px;width:1px;height:15px;background:#fff"></div>
  <div class="contact-item" style="left:903px">
    <svg width="12" height="12" viewBox="0 0 24 24"><path fill="#fff" d="M6.6 10.8a15 15 0 0 0 6.6 6.6l2.2-2.2c.3-.3.7-.4 1-.2 1.1.4 2.3.6 3.6.6.6 0 1 .4 1 1V20c0 .6-.4 1-1 1A17 17 0 0 1 3 4c0-.6.4-1 1-1h3.5c.6 0 1 .4 1 1 0 1.3.2 2.5.6 3.6.1.3 0 .7-.2 1z"/></svg>
    (123)-456-789
  </div>
</div>

<!-- header -->
<div class="brand" style="left:91px;top:40px">Quorvane</div>
<nav class="nav">
  <a href="#">Home</a><a href="#">What We Do</a><a href="#">About</a><a href="#">Projects</a>
</nav>
<a class="btn btn-outline" href="#" style="left:976px;top:50px;width:133px;height:38px">Contact
  <svg width="16" height="10" viewBox="0 0 16 10"><path d="M0 5h14M10 1l4 4-4 4" stroke="#0b0b0b" stroke-width="1.5" fill="none"/></svg></a>

<!-- hero -->
<section class="hero" role="img" aria-label="Engineering drawings on a desk with calipers, machined parts and a pen">
  <h1>Precision.<br>Efficiency. Clarity.</h1>
</section>
<a class="btn btn-light" href="#" style="left:528px;top:493px;width:141px;height:35px;font-size:14px">Get In Touch
  <svg width="13" height="13" viewBox="0 0 13 13"><path d="M1 12L12 1M4 1h8v8" stroke="#0b0b0b" stroke-width="1.4" fill="none"/></svg></a>
<svg class="abs" style="left:0;top:740px" width="1200" height="100" viewBox="0 0 1200 100" aria-hidden="true">
  <polygon points="0,64 1200,0 1200,100 0,100" fill="#fff"/>
  <polygon points="197,72 1200,11 1200,18 129,94" fill="#0b0b0b"/>
</svg>

<!-- about -->
<div class="photo" style="left:191px;top:931px;width:206px;height:345px;background:linear-gradient(180deg,#2c4f9e 0%,#5a7fc2 45%,#8b8a86 70%,#4d4a44 100%)" role="img" aria-label="Solar-powered monitoring station on a rocky summit"></div>
<div class="photo" style="left:408px;top:1021px;width:206px;height:345px;background:linear-gradient(180deg,#d9dcd6 0%,#5f7b4c 35%,#6b6962 70%,#4a4641 100%)" role="img" aria-label="Field technician beside a solar panel monitoring unit"></div>
<div class="badge">Quorvane</div>

<div class="mark-dot" style="left:667px;top:984px"></div>
<h2 class="section-title" style="left:667px;top:1021px">About Quorvane</h2>
<div class="rule" style="left:667px;top:1076px"></div>
<p class="about-copy">Welcome to Quorvane, your reliable partner in delivering innovative solutions. Our team of skilled professionals is committed to excellence, ensuring every project is handled with precision, efficiency, and integrity. We solve problems in the field, build robust infrastructure, and deliver accurate data to our clients. Let us help you achieve your goals with our tailored, sustainable solutions and exceptional service.</p>
<a class="btn btn-dark" href="#" style="left:667px;top:1257px;width:134px;height:36px">Learn More
  <svg width="13" height="13" viewBox="0 0 13 13"><path d="M1 12L12 1M4 1h8v8" stroke="#fff" stroke-width="1.4" fill="none"/></svg></a>

<!-- services -->
<div class="mark-dot" style="left:589px;top:1462px"></div>
<h2 class="section-title" style="left:0;width:1200px;text-align:center;top:1499px">Service We Provide</h2>
<div class="rule" style="left:565px;top:1553px"></div>

<div class="service service-field" style="background:linear-gradient(180deg,#e6e8ea 0%,#aab0b4 40%,#5e8a4a 65%,#3e6a33 100%)" role="img" aria-label="Survey instrument on a tripod in a green field">
  <div class="label">Fieldwork Solutions</div>
</div>
<div class="service service-positioning dark">
  <h3>Positioning And Monitoring</h3>
  <ul>
    <li>• Real-Time Kinematic (RTK) Solutions</li>
    <li>• Custom GNSS Base stations</li>
    <li>• NTRIP service</li>
    <li>• Tailored Monitoring Solutions</li>
    <li>• Environmental Monitoring</li>
    <li>• Robust communication Systems</li>
    <li>• Internet of Things (IoT) Integration</li>
    <li>• Solar powered systems</li>
    <li>• Smart Sensor Networks</li>
  </ul>
</div>
<div class="service service-design" style="background:linear-gradient(180deg,#4f8fd8 0%,#7fb0e4 35%,#d9dde0 60%,#3d4a3a 100%)" role="img" aria-label="Technician installing a dish on a mast above an equipment shelter">
  <div class="label">Design And Prototyping</div>
</div>

<!-- case studies -->
<div class="mark-dot" style="left:121px;top:2182px"></div>
<h2 class="section-title" style="left:121px;top:2219px">Case Studies</h2>
<div class="case-card">
  <h4>Remote camera installation in Alpine Environment.</h4>
  <p>Successful installation of advanced camera systems in the challenging and remote alpine regions of Fiordland. This installation supports Skyframe Pty Ltd in their environmental monitoring efforts, providing high-quality imagery and data to the Alpine Lands Trust from one of the most rugged and inaccessible areas in New Zealand.</p>
  <div class="arrows">
    <span class="off"><svg width="10" height="12" viewBox="0 0 10 12"><path d="M7 1L2 6l5 5" stroke="#888" stroke-width="1.5" fill="none"/></svg></span>
    <span><svg width="10" height="12" viewBox="0 0 10 12"><path d="M3 1l5 5-5 5" stroke="#0b0b0b" stroke-width="1.5" fill="none"/></svg></span>
  </div>
</div>
<div class="photo" style="left:578px;top:2154px;width:501px;height:417px;box-shadow:0 18px 40px rgba(0,0,0,.12);background:linear-gradient(180deg,#4d7fc7 0%,#a9c4e2 25%,#2e3b30 34%,#3a5f85 45%,#c8342e 75%,#2a2a2a 100%)" role="img" aria-label="Equipment case on the bow of a red inflatable boat in a fiord"></div>

<!-- quote -->
<section class="quote">
  <div class="mark-dot light" style="left:589px;top:55px"></div>
  <h2 class="section-title" style="left:0;width:1200px;text-align:center;top:92px;color:#fff">Get A Free Quote</h2>
  <div class="field" style="left:159px;top:175px;width:385px">Fast Name</div>
  <div class="field" style="left:625px;top:175px;width:385px">Last Name</div>
  <div class="field" style="left:159px;top:254px;width:385px">Enter Email</div>
  <div class="field" style="left:625px;top:254px;width:385px">Enter Phone</div>
  <div class="field" style="left:159px;top:330px;width:851px;height:72px">Enter Message</div>
  <div class="abs" style="left:0;top:475px;width:1200px;height:402px;background:linear-gradient(180deg,#0b0b0b 0%,#34455a 25%,#55647a 45%,#6b6b60 70%,#3a3a35 100%)" role="img" aria-label="Solar-powered monitoring station on an alpine ridge above mountain ranges"></div>
  <a class="btn btn-light" href="#" style="left:493px;top:436px;width:141px;height:35px">Submit Now
    <svg width="13" height="13" viewBox="0 0 13 13"><path d="M1 12L12 1M4 1h8v8" stroke="#0b0b0b" stroke-width="1.4" fill="none"/></svg></a>
  <svg class="abs" style="left:0;top:780px" width="1200" height="97" viewBox="0 0 1200 97" aria-hidden="true">
    <polygon points="0,97 1200,10 1200,97" fill="#0b0b0b"/>
    <polygon points="540,85 1070,5 1060,28" fill="#fff"/>
  </svg>
</section>

<!-- footer -->
<footer class="footer">
  <div class="brand" style="left:89px;top:62px;color:#fff">Quorvane</div>
  <p class="abs" style="left:89px;top:150px;width:340px;font-size:12.5px;line-height:16px">We are field operations experts with backgrounds in surveying, geoscience, and technical field work. Our purpose is to solve problems in the field, build robust infrastructure and deliver accurate data to our clients.</p>
  <h5 style="left:502px;top:42px">Quick Links</h5>
  <ul class="links"><li>Home</li><li>What We Do</li><li>About</li><li>Projects</li><li>Contact</li></ul>
  <h5 style="left:739px;top:42px">Subscribe To Our Newsletter</h5>
  <div class="newsletter">Enter Your Email
    <svg width="22" height="22" viewBox="0 0 24 24"><path d="M22 2L2 10l8 3 3 8z" fill="#0b0b0b"/><path d="M22 2L10 13" stroke="#fff" stroke-width="1.5"/></svg>
  </div>
  <div class="abs" style="left:89px;top:282px;width:1021px;height:1px;background:#666"></div>
  <div class="abs" style="left:0;top:305px;width:1200px;text-align:center;font-size:14px;font-weight:500">Copyright © Quorvane 2024. All Rights Reserved.</div>
  <div class="abs" style="left:1133px;top:261px;width:40px;height:40px;border-radius:50%;background:#fff;display:flex;align-items:center;justify-content:center">
    <svg width="10" height="7" viewBox="0 0 10 7"><path d="M1 6l4-4 4 4" stroke="#0b0b0b" stroke-width="1.6" fill="none"/></svg>
  </div>
</footer>

</body>
</html>
```